Luxurious Chocolate Box range for Varden + Pruitt Chocolate

New luxurious indulgent chocolate box packaging for Varden + Pruitt Chocolate cafe in New Zealand - Detailed design brief attached along with brand guidelines.

Objective

Develop a sophisticated, recyclable chocolate box range for Varden + Pruitt Chocolates that embodies contemporary elegance and luxury. The packaging must align with the brand’s identity and values, while being practical for scaling and environmentally conscious.

Product Overview
1. Packaging Sizes:
• Small: Fits 6-8 chocolates (e.g., gifting or personal indulgence).
• Medium: Fits 12-16 chocolates (ideal for sharing or thoughtful gifts).
• Large: Fits 20-24 chocolates (premium gifting).
2. Material Requirements:
• Recyclable or compostable materials with a luxury finish (e.g., kraft paper, WTB-certified cardboard).
• Avoid plastic; consider alternative closures (e.g., paper ribbon, magnetic fold).

Design Goals
1. Aesthetic:
• Clean, minimalistic design with subtle textures or patterns (e.g., marble effect, embossed logo).
• Use the brand’s colour palette: light moss green, white marble, and gold.
• Contemporary typography, with luxurious accents like foil stamping or debossing.
2. Functional Details:
• Modular inserts for chocolates to ensure secure fit.
• Scalable design: maintain visual consistency across sizes while enhancing the larger box’s impact.
• Easy to open and close, with the potential for reuse as a keepsake box.

3. Customer Experience:
• Unboxing should evoke indulgence: soft-touch materials, a liner with a quote or elegant tissue paper.
• Option for a personalized note card or gift message insert.

Sustainability Features
• Fully recyclable packaging materials, including any adhesives or inks.
• Encourage reusability by designing a box that doubles as a storage container.
• Minimal but impactful branding for long-term use without overprinting.

Content Elements
1. Front Panel:
• Logo and brand name (embossed or foiled).
• Box size description subtly integrated.
2. Interior:
• Branded liner (subtle print or embossed pattern).
• Optional message like “Crafted to delight.”
3. Back Panel:
• Short product description.
• Sustainability note: “Designed with care for you and the planet.”
• Required legal text (ingredients, allergens, weight, etc.).

Deliverables
1. Initial Concepts: Mood boards and material swatches.
2. Prototypes: Physical mockups for review and testing.
3. Final Artwork: Print-ready files (PDF, AI) for all box sizes.
4. Sustainability Documentation: Verification of materials and recyclability claims.

Timeline
• Week 1-2: Research and initial concepts.
• Week 3-4: Prototype development and feedback.
• Week 5: Finalize design, ready for production.

 

Sourcing Sustainable Materials for Varden + Pruitt Chocolate Box Range

To ensure the packaging aligns with the values of sustainability, while maintaining the luxurious and contemporary design of Varden + Pruitt Chocolates, here are some sustainable materials options to consider for your packaging:

Materials for the Boxes
1. Recyclable Cardboard
• WTB-certified Paperboard: Paperboard sourced from responsibly managed forests. This is a great option for creating sturdy yet eco-friendly boxes. It’s 100% recyclable and can be printed with eco-friendly inks.
• Recycled Paperboard: Made from post-consumer waste, recycled paperboard reduces the need for virgin materials. It’s slightly more textured, giving it a natural, rustic feel.
2. Kraft Paper
• Natural Kraft: An excellent eco-friendly option that is recyclable and biodegradable. It has a rough texture, providing an organic feel. It could be used for wrapping, or as a sturdy outer box.
• Bleached Kraft Paper: If a lighter, cleaner look is desired, bleached kraft is available in a white variant that still holds sustainable properties.
3. Plant-based Biodegradable Films
• If you wish to incorporate a soft-touch or shiny finish for premium appeal, consider using plant-based biodegradable films. These materials are made from renewable resources and decompose naturally in landfills. Examples include LumaWrap or PLA (Polylactic Acid) films, both of which are recyclable and compostable.

Inserts
1. Recycled Cardboard Inserts
• For secure placement of chocolates, recycled cardboard inserts are a great sustainable option. These inserts can be designed to hold the chocolates snugly, without the need for plastic.
2. Molded Paper Inserts
• Molded pulp is another biodegradable option made from recycled paper and wood fibers. It’s perfect for delicate chocolates, offering cushioning without plastic.
3. Biodegradable Foam Inserts
• If additional protection is needed, biodegradable foam made from starch or cellulose can be used to protect chocolates. These are eco-friendly alternatives to styrofoam.

Finishes & Printing
1. Eco-friendly Inks
• Use soy-based or vegetable-based inks for printing on paper and cardboard. These are less toxic and more sustainable than traditional petroleum-based inks. They also offer vibrant colors while being biodegradable.
2. Foil Stamping
• Water-based foil: Instead of using traditional foiling that involves plastic films, look for suppliers offering water-based foil options for a high-end finish. Gold or silver water-based foils provide a luxurious look while being more eco-conscious.

Unboxing Experience

Creating an unforgettable unboxing experience that aligns with Varden + Pruitt’s luxurious branding can be achieved with thoughtful use of sustainable materials:
1. Tissue Paper
• Use recycled tissue paper to line the interior. This adds an extra layer of elegance, offering protection to the chocolates while reinforcing your eco-friendly brand image.
• Optionally, printed tissue paper with a subtle, brand-related design (e.g., an embossed pattern or logo) could add a premium feel.
2. Ribbon or Closure
• Consider using paper ribbons or biodegradable twine for closures instead of plastic. For added elegance, you can use silk ribbon, which can be sustainably sourced.
• Magnetic closure on boxes could also give an upscale feel and would avoid the need for adhesives.
3. Personalized Note Card
• Include a recyclable card (printed on uncoated, eco-friendly paper) that can carry a brand message or a personalized greeting. This enhances the customer’s emotional connection to the product.

Next Steps
1. Sourcing Materials:
• Research suppliers that specialize in sustainable, luxury packaging. Companies such as Brindlecourt, Holvane Troske, and GreenParcelo are good starting points for sourcing eco-friendly and recyclable materials.
2. Testing and Prototypes:
• Once you’ve selected materials, work with a packaging manufacturer to create prototypes. Consider testing their durability, print quality, and overall presentation before moving forward with full-scale production.
3. Vendor Selection:
• Look for vendors who align with sustainability certifications, such as WTB, Loop to Root, and QMV 27305 for environmental standards. Ensure they are transparent about their processes.

Target Market(s)

Premium Chocolate Market

Industry/Entity Type

Chocolate Retail

Requirements
Must have
• Quality & indulgent look & feel
Nice to have
• Foil, Ribbons

```html
<!DOCTYPE html>
<html lang="en">
<head>
<meta charset="utf-8">
<title>Varden + Pruitt Chocolate – 24 Luxury Chocolates Box Artwork</title>
<link rel="stylesheet" href="https://fonts.googleapis.com/css2?family=Josefin+Sans:wght@300;400&display=swap">
<style>
  :root{
    --bg:#e4ede3;
    --cocoa:#0f0b07;
    --moss-panel:#dde7db;
    --moss-line:#c2d2c0;
    --gold-text:#cfa34f;
    --gold-dark:#a7792b;
    --gold-light:#f8dc8c;
    --ink:#1d1a16;
  }
  *{margin:0;padding:0;box-sizing:border-box}
  html,body{width:1200px;height:1200px;overflow:hidden;background:var(--bg)}
  body{font-family:"Josefin Sans",sans-serif;position:relative}

  .artwork{position:absolute;top:94px;left:452px;width:297px;height:1014px}

  .gold-band{
    background:linear-gradient(90deg,var(--gold-dark) 0%,var(--gold-light) 22%,#e6b955 50%,var(--gold-light) 78%,var(--gold-dark) 100%);
  }
  .moss-field{
    background:radial-gradient(ellipse at 55% 45%,#e3ece1 0%,var(--moss-panel) 60%,#d6e2d4 100%);
  }

  /* Side panel */
  .side-panel{position:absolute;left:0;top:0;width:44px;height:1014px;border-radius:4px;overflow:hidden;background:var(--moss-panel)}
  .side-panel .cap{height:276px;background:var(--cocoa);position:relative}
  .side-panel .gold-band{height:32px}
  .side-panel .body{position:absolute;top:308px;left:0;right:0;bottom:0}
  .vertical-label{
    position:absolute;left:50%;white-space:nowrap;
    transform:translate(-50%,-50%) rotate(-90deg);
    font-weight:300;font-size:14px;letter-spacing:1.4px;
  }
  .side-panel .cap .vertical-label{top:140px;color:var(--gold-text)}
  .side-panel .body .vertical-label{top:327px;color:var(--ink)}

  /* Front panel */
  .front-panel{position:absolute;left:69px;top:0;width:228px;height:1014px;border-radius:10px;overflow:hidden;background:var(--moss-panel)}
  .front-panel .cap{height:276px;background:var(--cocoa);text-align:center;color:var(--gold-text)}
  .brand{padding-top:86px}
  .brand-name{font-weight:400;font-size:17px;letter-spacing:2px;text-transform:uppercase;line-height:1}
  .brand-sub{font-weight:400;font-size:7px;letter-spacing:3.2px;text-transform:uppercase;margin-top:7px}
  .count{margin-top:56px;font-weight:300;font-size:14.5px;letter-spacing:1.6px;line-height:19px}
  .front-panel .gold-band{height:32px;display:flex;align-items:center;justify-content:center;
    font-weight:400;font-size:14px;letter-spacing:2.2px;color:var(--ink);padding-top:2px}
  .front-panel .pattern{position:absolute;top:308px;left:0;right:0;bottom:0}
  .weight{position:absolute;left:0;right:0;top:968px;text-align:center;font-size:13px;font-weight:400;color:var(--ink)}
</style>
</head>
<body>
  <main class="artwork">
    <section class="side-panel" aria-label="Side panel">
      <div class="cap"><span class="vertical-label">24 LUXURY CHOCOLATES</span></div>
      <div class="gold-band"></div>
      <div class="body moss-field"><span class="vertical-label">CRAFTED TO DELIGHT</span></div>
    </section>

    <section class="front-panel" aria-label="Front panel">
      <div class="cap">
        <div class="brand">
          <p class="brand-name">Varden + Pruitt</p>
          <p class="brand-sub">Chocolate Cafe</p>
        </div>
        <p class="count">24 LUXURY<br>CHOCOLATES</p>
      </div>
      <div class="gold-band">CRAFTED TO DELIGHT</div>
      <div class="pattern moss-field" role="img" aria-label="Fine line-drawn sweeping leaf pattern in soft moss green"></div>
      <p class="weight">200g</p>
    </section>
  </main>
</body>
</html>
```